Looking for a brindle ebook cover. Must meet all brindle press platform specifics. *

I need a book cover for my romance novel. The title is "Hearts, Unspoken". I would like this in typographic and an illustration below ( as a reference you can see Tall Tales by Doreen Platt). The author name is T V Nel. The story is set in England in the countryside, during fall and winter. It is a love/coming of age novel about a young couple. The girl is a writer, the boy is overcoming illness. The ending is tragic. The tone of the cover should convey an emotional read about true love and separation. It is a book for readers who enjoy novels by Bibi Tarns, Rosalind Voss, Doreen Platt.

Target Market(s)

Women in their 20s and 30s who enjoy romance.

Industry/Entity Type

Publishing

Font styles to use
Sans Serif

Requirements
Must have
• You can stress the title more than the author name on the cover.
Should not have
• No photographs.

```html
<!DOCTYPE html>
<html lang="en">
<head>
<meta charset="utf-8">
<title>Hearts, Unspoken — T V Nel</title>
<link rel="stylesheet" href="https://fonts.googleapis.com/css2?family=Abril+Fatface&family=Oswald:wght@500&family=Marcellus&display=swap">
<style>
  :root {
    --backdrop: #0b0b0b;
    --paper: #ffffff;
    --snow: #f5f5f8;
    --crimson: #e00a0a;
    --crimson-deep: #9e0505;
    --crimson-dark: #6e0303;
    --bridge-cream: #f2e6dc;
  }
  html, body {
    margin: 0;
    padding: 0;
    width: 1200px;
    height: 1200px;
    overflow: hidden;
    background: var(--backdrop);
  }
  .cover-canvas { display: block; width: 1200px; height: 1200px; }
  .title-main { font-family: "Abril Fatface", "Bodoni Moda", serif; font-size: 500px; }
  .title-sub {
    font-family: "Oswald", "Arial Narrow", sans-serif;
    font-weight: 500;
    font-size: 46px;
    fill: var(--snow);
  }
  .author-name {
    font-family: "Marcellus", "Cinzel", serif;
    font-size: 150px;
    fill: var(--snow);
  }
</style>
</head>
<body>
<svg class="cover-canvas" viewBox="0 0 1200 1200" xmlns="http://www.w3.org/2000/svg">
  <defs>
    <radialGradient id="red-wash" cx="0.5" cy="0.55" r="0.75">
      <stop offset="0" stop-color="var(--crimson)"/>
      <stop offset="0.6" stop-color="#c40808"/>
      <stop offset="1" stop-color="var(--crimson-deep)"/>
    </radialGradient>
    <linearGradient id="bridge-glow" x1="0" y1="0" x2="0" y2="1">
      <stop offset="0" stop-color="var(--bridge-cream)" stop-opacity="0.15"/>
      <stop offset="1" stop-color="var(--bridge-cream)" stop-opacity="0.85"/>
    </linearGradient>
    <clipPath id="paper-zone">
      <polygon points="224,48 975,48 975,318 900,326 800,340 700,360 600,385 480,406 380,432 300,456 224,466"/>
    </clipPath>
    <clipPath id="red-zone">
      <polygon points="224,466 300,456 380,432 480,406 600,385 700,360 800,340 900,326 975,318 975,1160 224,1160"/>
    </clipPath>
  </defs>

  <g class="cover">
    <rect class="cover-red" x="224" y="48" width="751" height="1112" fill="url(#red-wash)"/>
    <polygon class="cover-paper" fill="var(--paper)"
      points="224,48 975,48 975,318 900,326 800,340 700,360 600,385 480,406 380,432 300,456 224,466"/>

    <g class="title">
      <text class="title-main" x="355" y="540" textLength="503" lengthAdjust="spacingAndGlyphs"
            fill="var(--crimson)" clip-path="url(#paper-zone)">HEARTS</text>
      <text class="title-main" x="355" y="540" textLength="503" lengthAdjust="spacingAndGlyphs"
            fill="var(--snow)" clip-path="url(#red-zone)" aria-hidden="true">HEARTS</text>
      <text class="title-sub" x="358" y="621" textLength="500" lengthAdjust="spacing">UNSPOKEN</text>
    </g>

    <g class="author">
      <text class="author-name" x="600" y="790" text-anchor="middle">T.V</text>
      <text class="author-name" x="600" y="962" text-anchor="middle">NEL</text>
    </g>

    <rect class="bridge-illustration" x="335" y="1000" width="530" height="160"
          fill="url(#bridge-glow)" role="img"
          aria-label="Illustration: two small figures standing at either end of a broken bridge, birds scattering from the gap between them"/>
  </g>
</svg>
</body>
</html>
```